Awesome Beer Labels for food pairing

We are going to launch a range of craft beers specially brewed for food pairing, and we are in need of a logo and bottle labels to represent this. Every label individually has to show which beer type it is and the food groups it matches with. At the same time the whole range has to have the same appearance as we are promoting it as a whole package. As we are targeting middle-high to high class hospitality businesses we are looking for a luxurious, exclusive feel to the labels. We also need room for a clear title of the beer and a small food pairing description.

Industry/Entity Type

Craft Brewery

Font styles to use
Sans Serif
Decorative
Script

Colors

Designer to choose colors to be used in the design.

Requirements
Must have
• -Different beer labels where the style and name of the beer comes first, and the beer type second
• - A logo for the whole group which also has to be printed on glasses, so nothing to detailed.
• - Clear, recognizable pictures, drawings or symbols for the different food groups.
• - Room for the name of the beer, the beer type and a small description.
Nice to have
• An exclusive, luxurious look and feel that would not stand out in an high class restaurant.
• Something that combines the whole range of beers (something like a overlaying or connecting picture that combines alle the labels?)
Should not have
• To much different styles, the beers have to match

```html
<!DOCTYPE html>
<html lang="en">
<head>
<meta charset="utf-8">
<title>Tavola Brew – Food Pairing Labels</title>
<link href="https://fonts.googleapis.com/css2?family=Alfa+Slab+One&family=Montserrat:wght@400;500&family=UnifrakturMaguntia&display=swap" rel="stylesheet">
<style>
  :root{
    --bg-top:#f9e7b0;
    --bg-bottom:#e9bd5c;
    --gold:#f6e21a;
    --trim:#f2d23a;
    --ink:#ffffff;
    --ribbon-ink:#3a2a2a;
    --lager:#2a2391;
    --lager-dark:#15105a;
    --strong:#d0202f;
    --strong-dark:#8e0f1a;
    --brown:#4a3a34;
    --brown-dark:#241a16;
    --ipa:#c8566a;
    --ipa-dark:#8e2f40;
  }
  *{box-sizing:border-box;margin:0;padding:0}
  html,body{width:946px;height:1200px;overflow:hidden}
  body{
    background:linear-gradient(180deg,var(--bg-top) 0%,var(--bg-bottom) 100%);
    font-family:"Montserrat",sans-serif;
  }
  .label-range{
    position:absolute;inset:0;
    display:grid;
    grid-template-columns:340px 340px;
    grid-template-rows:460px 460px;
    gap:60px;
    justify-content:center;
    align-content:center;
  }
  .label{position:relative;width:340px;height:460px}
  .label__shape{position:absolute;inset:0}
  .label--lager{--face:var(--lager);--edge:var(--lager-dark)}
  .label--strong{--face:var(--strong);--edge:var(--strong-dark)}
  .label--brown{--face:var(--brown);--edge:var(--brown-dark)}
  .label--ipa{--face:var(--ipa);--edge:var(--ipa-dark)}
  .label__content{
    position:absolute;inset:0;
    display:flex;flex-direction:column;align-items:center;
    padding-top:62px;color:var(--ink);
  }
  .brand{
    display:flex;align-items:center;gap:22px;height:50px;
  }
  .brand__wheat{width:26px;height:46px;border-radius:13px;background:rgba(255,255,255,.35)}
  .brand__name{
    display:flex;align-items:center;gap:6px;
    font-family:"Montserrat",sans-serif;font-weight:500;font-size:13px;letter-spacing:2px;
  }
  .brand__dot{width:10px;height:10px;border-radius:50%;background:var(--ink)}
  .label__title{
    font-family:"Alfa Slab One",serif;
    font-size:86px;line-height:1;color:var(--gold);
    margin-top:14px;letter-spacing:-1px;
  }
  .label__type{
    font-family:"Montserrat",sans-serif;font-weight:400;
    font-size:22px;letter-spacing:3px;margin-top:4px;white-space:nowrap;
  }
  .ribbon{position:relative;width:220px;height:26px;margin-top:8px}
  .ribbon svg{position:absolute;inset:0}
  .ribbon__text{
    position:relative;display:block;text-align:center;line-height:26px;
    font-family:"UnifrakturMaguntia",cursive;font-size:14px;color:var(--ribbon-ink);
  }
  .pairing-icon{
    width:96px;height:56px;margin-top:26px;border-radius:8px;
    background:rgba(255,255,255,.85);
  }
</style>
</head>
<body>
<main class="label-range">

  <article class="label label--lager">
    <svg class="label__shape" viewBox="0 0 340 460" aria-hidden="true">
      <polygon points="170,0 340,90 340,370 170,460 0,370 0,90" fill="var(--edge)"/>
      <polygon points="170,12 328,96 328,364 170,448 12,364 12,96" fill="var(--face)" stroke="var(--trim)" stroke-width="2"/>
      <polygon points="170,26 314,104 314,356 170,434 26,356 26,104" fill="none" stroke="#fff" stroke-width="1" stroke-dasharray="3 3"/>
    </svg>
    <div class="label__content">
      <div class="brand">
        <div class="brand__wheat" role="img" aria-label="Wheat sprig ornament"></div>
        <span class="brand__name"><span class="brand__dot"></span>TAVOLA BREW</span>
        <div class="brand__wheat" role="img" aria-label="Wheat sprig ornament"></div>
      </div>
      <h2 class="label__title">BEER</h2>
      <p class="label__type">LAGER PALE</p>
      <div class="ribbon">
        <svg viewBox="0 0 220 26" aria-hidden="true"><polygon points="0,3 220,3 208,13 220,23 0,23 12,13" fill="#fff"/></svg>
        <span class="ribbon__text">best assortment with fish</span>
      </div>
      <div class="pairing-icon" role="img" aria-label="Fish icon for seafood pairing"></div>
    </div>
  </article>

  <article class="label label--strong">
    <svg class="label__shape" viewBox="0 0 340 460" aria-hidden="true">
      <polygon points="170,0 340,90 340,370 170,460 0,370 0,90" fill="var(--edge)"/>
      <polygon points="170,12 328,96 328,364 170,448 12,364 12,96" fill="var(--face)" stroke="var(--trim)" stroke-width="2"/>
      <polygon points="170,26 314,104 314,356 170,434 26,356 26,104" fill="none" stroke="#fff" stroke-width="1" stroke-dasharray="3 3"/>
    </svg>
    <div class="label__content">
      <div class="brand">
        <div class="brand__wheat" role="img" aria-label="Wheat sprig ornament"></div>
        <span class="brand__name"><span class="brand__dot"></span>TAVOLA BREW</span>
        <div class="brand__wheat" role="img" aria-label="Wheat sprig ornament"></div>
      </div>
      <h2 class="label__title">BEER</h2>
      <p class="label__type">STRONG ALE</p>
      <div class="ribbon">
        <svg viewBox="0 0 220 26" aria-hidden="true"><polygon points="0,3 220,3 208,13 220,23 0,23 12,13" fill="#fff"/></svg>
        <span class="ribbon__text">best assortment with beef</span>
      </div>
      <div class="pairing-icon" role="img" aria-label="Cow icon for beef pairing"></div>
    </div>
  </article>

  <article class="label label--brown">
    <svg class="label__shape" viewBox="0 0 340 460" aria-hidden="true">
      <polygon points="170,0 340,90 340,370 170,460 0,370 0,90" fill="var(--edge)"/>
      <polygon points="170,12 328,96 328,364 170,448 12,364 12,96" fill="var(--face)" stroke="var(--trim)" stroke-width="2"/>
      <polygon points="170,26 314,104 314,356 170,434 26,356 26,104" fill="none" stroke="#fff" stroke-width="1" stroke-dasharray="3 3"/>
    </svg>
    <div class="label__content">
      <div class="brand">
        <div class="brand__wheat" role="img" aria-label="Wheat sprig ornament"></div>
        <span class="brand__name"><span class="brand__dot"></span>TAVOLA BREW</span>
        <div class="brand__wheat" role="img" aria-label="Wheat sprig ornament"></div>
      </div>
      <h2 class="label__title">BEER</h2>
      <p class="label__type">BROWN ALE</p>
      <div class="ribbon">
        <svg viewBox="0 0 220 26" aria-hidden="true"><polygon points="0,3 220,3 208,13 220,23 0,23 12,13" fill="#fff"/></svg>
        <span class="ribbon__text">best assortment with chiken</span>
      </div>
      <div class="pairing-icon" role="img" aria-label="Roast chicken icon for poultry pairing"></div>
    </div>
  </article>

  <article class="label label--ipa">
    <svg class="label__shape" viewBox="0 0 340 460" aria-hidden="true">
      <polygon points="170,0 340,90 340,370 170,460 0,370 0,90" fill="var(--edge)"/>
      <polygon points="170,12 328,96 328,364 170,448 12,364 12,96" fill="var(--face)" stroke="var(--trim)" stroke-width="2"/>
      <polygon points="170,26 314,104 314,356 170,434 26,356 26,104" fill="none" stroke="#fff" stroke-width="1" stroke-dasharray="3 3"/>
    </svg>
    <div class="label__content">
      <div class="brand">
        <div class="brand__wheat" role="img" aria-label="Wheat sprig ornament"></div>
        <span class="brand__name"><span class="brand__dot"></span>TAVOLA BREW</span>
        <div class="brand__wheat" role="img" aria-label="Wheat sprig ornament"></div>
      </div>
      <h2 class="label__title">BEER</h2>
      <p class="label__type">INDIA PALE ALE</p>
      <div class="ribbon">
        <svg viewBox="0 0 220 26" aria-hidden="true"><polygon points="0,3 220,3 208,13 220,23 0,23 12,13" fill="#fff"/></svg>
        <span class="ribbon__text">best assortment with porc</span>
      </div>
      <div class="pairing-icon" role="img" aria-label="Pig icon for pork pairing"></div>
    </div>
  </article>

</main>
</body>
</html>
```